Vexora Design Project

International Travel agent, need a vexora design. We romote family travel destinations, Malrow, Kelvane Studios, and cruises.

Travel

```html
<!DOCTYPE html>
<html lang="en">
<head>
<meta charset="utf-8">
<title>Wander Joy Trips — Vexora profile</title>
<link href="https://fonts.googleapis.com/css2?family=Arimo:wght@400;700&family=Gelasio:ital@1&display=swap" rel="stylesheet">
<style>
:root{
  --page:#f2f2f2;
  --bar-top:#3a3a3a;
  --bar-bottom:#1f1f1f;
  --nav-text:#bfbfbf;
  --panel:#ffffff;
  --border:#d6d6d6;
  --divider:#e6e6e6;
  --ink:#333333;
  --muted:#999999;
  --link:#0a84c6;
  --brand:#174f9a;
  --brand-light:#5aa3dc;
  --verified:#2aa9e0;
  --button:#eeeeee;
  --action:#2d8ddf;
}
*{box-sizing:border-box;margin:0;padding:0}
html,body{width:1200px;height:900px;overflow:hidden}
body{position:relative;background:var(--page);font-family:"Arimo",Arial,sans-serif;color:var(--ink);font-size:13px}
.topbar{position:absolute;left:0;top:0;width:1200px;height:36px;background:linear-gradient(var(--bar-top),var(--bar-bottom))}
.topnav{position:absolute;left:280px;top:0;height:36px;display:flex;align-items:center;gap:22px;color:var(--nav-text);font-weight:700;font-size:13px}
.topnav span{display:flex;align-items:center;gap:6px}
.topbar .brandmark{position:absolute;left:689px;top:8px;color:#777;font-weight:700;font-size:12px}
.search{position:absolute;left:801px;top:4px;width:202px;height:25px;border-radius:13px;background:#555;border:1px solid #666;color:#ccc;font-size:13px;display:flex;align-items:center;gap:6px;padding-left:9px}
.usermenu{position:absolute;left:1016px;top:4px;width:50px;height:26px;border-left:1px solid #444;display:flex;align-items:center;justify-content:center;gap:4px}
.compose{position:absolute;left:1082px;top:3px;width:36px;height:27px;border-radius:4px;background:var(--action);border:1px solid #1b6db5;display:flex;align-items:center;justify-content:center}

.sidebar{position:absolute;left:0;top:36px;width:280px;text-align:center}
.logo{margin:22px auto 0;width:200px;height:150px;display:flex;flex-direction:column;align-items:center;justify-content:center;gap:8px}
.logo .dot{width:48px;height:48px;border-radius:50%;background:var(--brand-light)}
.logo .name{font-weight:700;font-size:24px;color:var(--brand);line-height:1.05}
.contact{margin-top:22px}
.contact-item{margin-bottom:25px}
.contact-icon{width:40px;height:40px;border-radius:50%;background:var(--brand);margin:0 auto 6px;display:flex;align-items:center;justify-content:center}
.contact-label{color:var(--brand);font-size:14px}
.contact-value{font-size:12px;color:#222;margin-top:4px;line-height:1.35}

.panel{position:absolute;background:var(--panel);border:1px solid var(--border);border-radius:5px}
.profile{left:283px;top:52px;width:835px;height:151px}
.avatar-lg{position:absolute;left:6px;top:26px;width:126px;height:96px;display:flex;align-items:center;justify-content:center;text-align:center;color:var(--brand);font-weight:700;font-size:17px;line-height:1.05}
.profile-name{position:absolute;left:150px;top:12px;font-size:29px;font-weight:700;color:#333;display:flex;align-items:center;gap:14px}
.verified{width:22px;height:22px;border-radius:50%;background:var(--verified)}
.profile-handle{position:absolute;left:151px;top:47px;font-size:18px;color:var(--muted)}
.profile-bio{position:absolute;left:152px;top:72px;width:400px;font-family:"Gelasio",Georgia,serif;font-style:italic;font-size:14px;color:#555;line-height:1.3}
.profile-meta{position:absolute;left:153px;top:109px;font-size:12px;color:#555;display:flex;gap:26px}
.profile-meta a{color:var(--link);text-decoration:none}
.follow-btn{position:absolute;left:692px;top:11px;width:86px;height:30px;border:1px solid #ccc;border-radius:4px;background:linear-gradient(#fff,var(--button));font-weight:700;font-size:14px;display:flex;align-items:center;justify-content:center;gap:6px}
.follow-btn .sq{width:13px;height:10px;border-radius:2px;background:var(--verified)}
.more-btn{position:absolute;left:782px;top:11px;width:38px;height:30px;border:1px solid #ccc;border-radius:4px;background:linear-gradient(#fff,var(--button));display:flex;align-items:center;justify-content:center}
.stats{position:absolute;left:692px;top:49px;width:131px}
.stat{height:31px;border-bottom:1px solid var(--divider);display:flex;align-items:center;gap:5px;font-size:13px;font-weight:700}
.stat:last-child{border-bottom:0}
.stat small{font-size:10px;color:var(--muted);font-weight:400;letter-spacing:.3px}

.tweets-to{left:283px;top:215px;width:300px;height:82px;padding:12px 9px}
.tweets-to h3,.feed h2{font-size:14px;font-weight:700}
.tweets-to .input{margin-top:7px;height:31px;border:1px solid #ccc;border-radius:4px;color:#aaa;font-size:12px;padding:8px 10px}

.menu{left:283px;top:309px;width:300px;height:294px}
.menu-item{height:35.5px;border-bottom:1px solid var(--divider);display:flex;align-items:center;justify-content:space-between;padding:0 9px;color:var(--link);font-size:14px}
.menu-item.active{color:#333;font-weight:700}
.menu-item.images{border-bottom:0}
.thumbs{display:flex;gap:9px;padding:0 9px}
.thumb{width:66px;height:66px}
.thumb.one{background:linear-gradient(160deg,#3d5f7a,#8a5a38)}
.thumb.two{background:linear-gradient(160deg,#5b7a3f,#a39a86)}

.similar{left:283px;top:614px;width:300px;height:194px}
.similar-head{height:34px;border-bottom:1px solid var(--divider);display:flex;align-items:center;justify-content:space-between;padding:0 9px;color:var(--link);font-size:14px}
.person{display:flex;gap:9px;padding:9px 11px 0;height:42px}
.person .pic{width:32px;height:32px;background:linear-gradient(#4a3a30,#2a2424)}
.person .who{font-size:12px;color:#333}
.person .who span{color:#bbb;margin-left:32px}
.person .who b{display:block;color:var(--link);font-weight:700;margin-top:4px;font-size:12px}

.feed{left:598px;top:215px;width:520px;height:593px}
.feed h2{font-size:18px;padding:12px 10px;height:44px;border-bottom:1px solid var(--divider)}
.tweet{position:relative;height:73px;border-bottom:1px solid var(--divider);padding:9px 10px 0 67px;font-size:14px;line-height:1.25}
.tweet .av{position:absolute;left:5px;top:13px;width:54px;height:40px;display:flex;align-items:center;justify-content:center;text-align:center;color:var(--brand);font-weight:700;font-size:9px;line-height:1}
.tweet .head{display:flex;gap:8px;font-size:13.5px;margin-bottom:3px}
.tweet .head b{color:#333}
.tweet .head span{color:#aaa;font-size:12px}
.tweet .time{position:absolute;right:12px;top:10px;color:#999;font-size:12px}
.tweet a{color:var(--link);text-decoration:none}

.scene{position:absolute;left:900px;top:780px;width:300px;height:120px;border-radius:150px 150px 0 0;background:radial-gradient(ellipse at 40% 80%,#3b6fc4,#8ab8e6 60%,rgba(220,232,245,0) 75%)}
</style>
</head>
<body>
<header class="topbar">
  <nav class="topnav">
    <span><svg width="18" height="16" viewBox="0 0 18 16"><path d="M9 1 1 8h2v7h4v-4h4v4h4V8h2z" fill="#bfbfbf"/></svg>Home</span>
    <span><svg width="18" height="18" viewBox="0 0 18 18"><circle cx="9" cy="9" r="7.5" fill="none" stroke="#bfbfbf" stroke-width="2"/><circle cx="9" cy="9" r="3" fill="none" stroke="#bfbfbf" stroke-width="2"/></svg>Connect</span>
    <span><svg width="16" height="16" viewBox="0 0 16 16"><path d="M5 1 3 15M12 1l-2 14M1 5h14M1 11h14" stroke="#bfbfbf" stroke-width="2"/></svg>Discover</span>
  </nav>
  <div class="brandmark">Vexora</div>
  <div class="search"><svg width="12" height="12" viewBox="0 0 12 12"><circle cx="5" cy="5" r="3.8" fill="none" stroke="#ccc" stroke-width="1.6"/><path d="m8 8 3 3" stroke="#ccc" stroke-width="1.6"/></svg>Search</div>
  <div class="usermenu"><svg width="20" height="18" viewBox="0 0 20 18"><circle cx="10" cy="6" r="4.5" fill="#aaa"/><path d="M2 18c0-5 4-7 8-7s8 2 8 7z" fill="#aaa"/></svg><svg width="8" height="5"><path d="M0 0h8L4 5z" fill="#aaa"/></svg></div>
  <div class="compose"><svg width="18" height="16" viewBox="0 0 18 16"><rect x="1" y="3" width="12" height="12" fill="none" stroke="#fff" stroke-width="1.6"/><path d="m7 10 9-9" stroke="#fff" stroke-width="2"/></svg></div>
</header>

<aside class="sidebar">
  <div class="logo"><div class="dot"></div><div class="name">Wander Joy<br>Trips</div></div>
  <div class="contact">
    <div class="contact-item">
      <div class="contact-icon"><svg width="22" height="22" viewBox="0 0 22 22"><circle cx="11" cy="11" r="9" fill="none" stroke="#fff" stroke-width="2"/><circle cx="11" cy="11" r="3.5" fill="none" stroke="#fff" stroke-width="2"/></svg></div>
      <div class="contact-label">Business Trading Address :</div>
      <div class="contact-value">Av. Lumen 240, 2 piso, Col.<br>Arboleda, Ciudad Norte 06520</div>
    </div>
    <div class="contact-item">
      <div class="contact-icon"><svg width="20" height="24" viewBox="0 0 20 24"><path d="M6 2c-3 1-4 4-3 9s5 10 9 11c2 0 3-1 4-2l-3-5-3 1c-2-2-3-5-3-8l3-1z" fill="#fff"/></svg></div>
      <div class="contact-label">Telephone :</div>
      <div class="contact-value">(55) 5210-4836 (O), (55) 9342-7185 (M)</div>
    </div>
    <div class="contact-item">
      <div class="contact-icon"><svg width="24" height="18" viewBox="0 0 24 18"><rect x="1" y="1" width="22" height="16" rx="1" fill="#fff"/><path d="m1 1 11 9 11-9" fill="none" stroke="#174f9a" stroke-width="1.6"/></svg></div>
      <div class="contact-label">Email :</div>
      <div class="contact-value">elena@wanderjoytrips.com</div>
    </div>
    <div class="contact-item">
      <div class="contact-icon"><svg width="22" height="22" viewBox="0 0 22 22"><rect x="3" y="9" width="10" height="6" rx="3" transform="rotate(-45 8 12)" fill="none" stroke="#fff" stroke-width="2.2"/><rect x="9" y="7" width="10" height="6" rx="3" transform="rotate(-45 14 10)" fill="none" stroke="#fff" stroke-width="2.2"/></svg></div>
      <div class="contact-label">Website :</div>
      <div class="contact-value">www.wanderjoytrips.com</div>
    </div>
  </div>
</aside>

<section class="panel profile">
  <div class="avatar-lg">Wander Joy<br>Trips</div>
  <h1 class="profile-name">Wander Joy Trips <span class="verified"></span></h1>
  <div class="profile-handle">@wanderjoy</div>
  <p class="profile-bio">Este puente aprovechen y disgruntlement de las Maravillosas playas de mexico</p>
  <div class="profile-meta"><span>Mexico City</span><a href="#">http://www.wanderjoytrips.com/</a></div>
  <div class="follow-btn"><span class="sq"></span>Follow</div>
  <div class="more-btn"><svg width="22" height="14" viewBox="0 0 22 14"><circle cx="7" cy="4" r="3.5" fill="#555"/><path d="M0 14c0-4 3-5 7-5s7 1 7 5z" fill="#555"/><path d="M16 6h6l-3 4z" fill="#555"/></svg></div>
  <div class="stats">
    <div class="stat">1,693 <small>TWEETS</small></div>
    <div class="stat">141 <small>FOLLOWING</small></div>
    <div class="stat">307,156 <small>FOLLOWERS</small></div>
  </div>
</section>

<section class="panel tweets-to">
  <h3>Tweets to Wander Joy Trips</h3>
  <div class="input">@ wanderjoy</div>
</section>

<nav class="panel menu">
  <div class="menu-item active">Tweets <svg width="8" height="12"><path d="m1 1 5 5-5 5" fill="none" stroke="#555" stroke-width="2"/></svg></div>
  <div class="menu-item">Following <svg width="8" height="12"><path d="m1 1 5 5-5 5" fill="none" stroke="#bbb" stroke-width="2"/></svg></div>
  <div class="menu-item">Followers <svg width="8" height="12"><path d="m1 1 5 5-5 5" fill="none" stroke="#bbb" stroke-width="2"/></svg></div>
  <div class="menu-item">Favourites <svg width="8" height="12"><path d="m1 1 5 5-5 5" fill="none" stroke="#bbb" stroke-width="2"/></svg></div>
  <div class="menu-item">Lists <svg width="8" height="12"><path d="m1 1 5 5-5 5" fill="none" stroke="#bbb" stroke-width="2"/></svg></div>
  <div class="menu-item images">Recent images <svg width="8" height="12"><path d="m1 1 5 5-5 5" fill="none" stroke="#bbb" stroke-width="2"/></svg></div>
  <div class="thumbs">
    <div class="thumb one" role="img" aria-label="Photo of a framed sign in a wooden interior"></div>
    <div class="thumb two" role="img" aria-label="Photo of a group outdoors under trees"></div>
  </div>
</nav>

<section class="panel similar">
  <div class="similar-head">Similar to Wander Joy Trips <svg width="8" height="12"><path d="m1 1 5 5-5 5" fill="none" stroke="#bbb" stroke-width="2"/></svg></div>
  <div class="person"><div class="pic" role="img" aria-label="Profile photo"></div><div class="who">Owen Hartley<span>@ohartley</span><b>Follow</b></div></div>
  <div class="person"><div class="pic" role="img" aria-label="Profile photo"></div><div class="who">lucas ferrand<span>@lucasferrand</span><b>Follow</b></div></div>
  <div class="person"><div class="pic" role="img" aria-label="Profile photo"></div><div class="who">Martin Reyes<span>@mreyes</span><b>Follow</b></div></div>
</section>

<section class="panel feed">
  <h2>Tweets</h2>
  <article class="tweet"><div class="av">Wander Joy<br>Trips</div><div class="head"><b>Wander Joy Trips</b><span>@wanderjoy</span></div><span class="time">14h</span>Welcome to everything under the sun with <a href="#">@CruiseNordvik</a> in the Caribbean: relaxation, pampering, new views every day. <a href="#">#cruise</a></article>
  <article class="tweet"><div class="av">Wander Joy<br>Trips</div><div class="head"><b>Wander Joy Trips</b><span>@wanderjoy</span></div><span class="time">14h</span>Un #crucero por los ríos de Europa, Africa, es una maravillosa forma de conocer descansar y viajar</article>
  <article class="tweet"><div class="av">Wander Joy<br>Trips</div><div class="head"><b>Wander Joy Trips</b><span>@wanderjoy</span></div><span class="time">14h</span>Good morning all... it's about time to get up, get out and #getafterit! Who's fitting a workout into their schedule today?</article>
  <article class="tweet"><div class="av">Wander Joy<br>Trips</div><div class="head"><b>Wander Joy Trips</b><span>@wanderjoy</span></div><span class="time">14h</span>Agosto casi termina se acerca el puente de septiembre hay que reservar y visitar <a href="#">#campeche</a></article>
  <article class="tweet"><div class="av">Wander Joy<br>Trips</div><div class="head"><b>Wander Joy Trips</b><span>@wanderjoy</span></div><span class="time">14h</span>Good morning all... it's about time to get up, get out and #getafterit! Who's fitting a workout into their schedule today?</article>
  <article class="tweet"><div class="av">Wander Joy<br>Trips</div><div class="head"><b>Wander Joy Trips</b><span>@wanderjoy</span></div><span class="time">14h</span>Good morning all... it's about time to get up, get out and #getafterit! Who's fitting a workout into their schedule today?</article>
  <article class="tweet"><div class="av">Wander Joy<br>Trips</div><div class="head"><b>Wander Joy Trips</b><span>@wanderjoy</span></div><span class="time">14h</span>Good morning all... it's about time to get up, get out and #getafterit! Who's fitting a workout into their schedule today?</article>
</section>

<div class="scene" role="img" aria-label="Illustration of two cheerful travellers riding a blue cartoon airplane"></div>
</body>
</html>
```